BrightmoorCA Cleaning Service Truck Signage

We want a truck sign design for a new Carpet cleaning and janitorial service near the beach cities of Oxnard, Ventura and Camarillo, California. The company name should be in a bright green, clean font in a flowing cursive style with capital 'CA' at the end , all one word. Use a dark drop-shadow or effect to make the name stand out boldly on a white background. The company 800 number should be bold, just below the name. The mascot should have elements of the soldier,shield, and the cleaning wand in place of the sword. Use the photos of Marcus to incorporate any facial elements possible, with the hair 'curl' like Marcus has.
The overall look should be clean, clear, bright and professional with an upbeat mascot.
We are a local family business, friendly, prompt always professional and we guarantee satisfaction always!
Updates

I have added 2 photos of the van for you as you work on your designs.Thank youRick G Added Saturday, September 17, 2016

Target Market(s)

Residential Carpet cleaning customers and local small-mid size businesses such as medical clinics identified as ideal commercial clients.

Industry/Entity Type

Cleaning Service

Contact Information for Business Card

Company name in top left. Mascot to the far right of that.
Dale Petrov - Owner.
Phone: 866-417-3052
email: dale@brightmoorca-example.com
website: www.brightmoorca-example.com

Font styles to use
Script

Colors
00a990
ffffff
0392cd
33a6d7
33b8a4

Requirements
Must have
• A Clean, bright professionally designed image. The mascot should have elements of the soldier,shield, and the cleaning wand in place of the sword. Use the photos of Marcus to incorporate any facial elements possible, with the hair 'curl' like Marcus has.
• The overall look should be clean, clear, bright and professional with an upbeat mascot.
• We are a local family business, friendly, prompt always professional and we guarantee satisfaction always!
Nice to have
• Possibly include: Our area is called the 'Gold Coast'. Slogan: Bright moor, satisfaction guaranteed.
Should not have
• too many colors.

```html
<!DOCTYPE html>
<html lang="en">
<head>
<meta charset="utf-8">
<title>Brightmoor CA – Van Signage</title>
<link rel="stylesheet" href="https://fonts.googleapis.com/css2?family=Questrial&family=Yellowtail&display=swap">
<style>
  :root {
    --teal: #00a990;
    --teal-light: #33b8a4;
    --ink: #1b1b1b;
    --red: #d3343f;
    --white: #ffffff;
    --backdrop: #eef1f2;
    --photo: #9aa3a6;
    --mascot: #7fb9a4;
  }
  * { margin: 0; padding: 0; box-sizing: border-box; }
  html, body { width: 1200px; height: 732px; overflow: hidden; background: var(--backdrop); }
  .canvas { position: relative; width: 1200px; height: 732px; font-family: "Questrial", sans-serif; color: var(--ink); }
  .wrap-panel { position: absolute; left: 128px; top: 316px; width: 944px; height: 308px; background: var(--white); border-radius: 26px; box-shadow: 0 2px 10px rgba(0,0,0,.08); }
  .accent { position: absolute; left: 0; top: 0; }
  .brand-name { position: absolute; left: 188px; top: 334px; font-size: 50px; font-weight: 400; line-height: 56px; color: var(--teal); letter-spacing: -0.5px; }
  .phone { position: absolute; left: 186px; top: 392px; font-size: 42px; font-weight: 700; line-height: 48px; color: var(--ink); letter-spacing: -0.5px; }
  .owner-photo { position: absolute; left: 132px; top: 448px; width: 92px; height: 160px; background: linear-gradient(180deg, var(--photo), #cfd4d6); }
  .area-tag { position: absolute; left: 244px; top: 531px; display: flex; align-items: center; gap: 6px; color: var(--white); font-size: 14px; line-height: 18px; }
  .region-script { position: absolute; left: 348px; top: 482px; font-family: "Yellowtail", cursive; font-size: 32px; line-height: 40px; color: var(--red); }
  .service-list { position: absolute; list-style: none; font-size: 22px; line-height: 28px; }
  .service-list li::before { content: "•"; font-size: 13px; margin-right: 8px; vertical-align: 3px; }
  .service-list.surfaces { left: 530px; top: 476px; }
  .service-list.sectors { left: 768px; top: 464px; font-size: 23px; line-height: 28px; }
  .mascot { position: absolute; left: 684px; top: 460px; width: 72px; height: 142px; border-radius: 30px 30px 14px 14px; background: radial-gradient(circle at 50% 35%, var(--mascot), #c9ddd3); }
  .slogan { position: absolute; left: 468px; top: 582px; font-size: 13px; line-height: 18px; }
  .base-stripe { position: absolute; left: 468px; top: 604px; width: 428px; height: 12px; background: var(--teal); }
</style>
</head>
<body>
<main class="canvas">
  <div class="wrap-panel"></div>

  <svg class="accent" width="1200" height="732" aria-hidden="true">
    <polygon points="132,448 256,448 344,548 344,608 132,608" fill="var(--teal)"/>
  </svg>

  <h1 class="brand-name">Brightmoor CA</h1>
  <p class="phone">(866) 417-3052</p>

  <div class="owner-photo" role="img" aria-label="Photo of Marcus wearing a company T-shirt"></div>

  <p class="area-tag">
    <svg width="12" height="18" viewBox="0 0 12 18" aria-hidden="true">
      <path d="M6 1 C2.5 1 1 3.6 1 6 C1 10 6 17 6 17 C6 17 11 10 11 6 C11 3.6 9.5 1 6 1 Z" fill="none" stroke="var(--white)" stroke-width="1.6"/>
      <circle cx="6" cy="6" r="1.8" fill="var(--white)"/>
    </svg>
    Gold Coast
  </p>

  <p class="region-script">California</p>

  <ul class="service-list surfaces">
    <li>Carpet</li>
    <li>Tile</li>
    <li>Floors</li>
  </ul>

  <div class="mascot" role="img" aria-label="Mascot: helmeted soldier holding a shield and a cleaning wand"></div>

  <ul class="service-list sectors">
    <li>Residential</li>
    <li>Commercial</li>
    <li>Building</li>
    <li>Maintenance</li>
  </ul>

  <p class="slogan">Bright moor, satisfaction guaranteed</p>
  <div class="base-stripe"></div>
</main>
</body>
</html>
```